GLOW RIDGE 21 DAY Challange

looking to make a poster that needs to be 36" wide x24"tall design graphic . Check out the added file as it is a rough draft of the material I would like it to say.

Phone number 555-302-4418 www.rgchiropractic..com

Adults aged 25-45 high income adults needing to make changes in dies and lose weight

```html
<!DOCTYPE html>
<html lang="en">
<head>
<meta charset="utf-8">
<title>Glow Ridge 21 Day Challange</title>
<link href="https://fonts.googleapis.com/css2?family=Bebas+Neue&family=Advent+Pro:wght@200;300&family=Open+Sans:wght@400;700;800&display=swap" rel="stylesheet">
<style>
  :root {
    --red: #e8202a;
    --navy: #2e2f8f;
    --white: #ffffff;
    --ink: #1a1a1a;
    --bg-top: #9aa4b1;
    --bg-bottom: #c3c9d1;
    --crowd-light: #b4a8a4;
    --crowd-mid: #7a5e5c;
    --crowd-dark: #3a3436;
  }
  * { margin: 0; padding: 0; box-sizing: border-box; }
  html, body { width: 1200px; height: 800px; overflow: hidden; }
  body { font-family: "Open Sans", Arial, sans-serif; }
  .poster {
    position: relative; width: 1200px; height: 800px; overflow: hidden;
    background: linear-gradient(160deg, var(--bg-top), var(--bg-bottom));
  }
  .crowd-photo {
    position: absolute; left: 300px; top: 30px; width: 900px; height: 570px;
    border-radius: 60px 60px 0 0;
    background: linear-gradient(180deg, var(--crowd-light) 0%, var(--crowd-mid) 45%, var(--crowd-dark) 100%);
    opacity: .8;
  }
  .swoosh { position: absolute; inset: 0; }
  .brand {
    position: absolute; left: 48px; top: 28px;
    display: flex; align-items: center; gap: 10px;
    font-weight: 800; font-size: 25px; color: var(--white); letter-spacing: .5px;
  }
  .brand-mark { width: 22px; height: 22px; background: var(--white); }
  .headline { position: absolute; left: 48px; top: 120px; line-height: 1; font-weight: 400; }
  .headline-name { font-family: "Bebas Neue", Impact, sans-serif; color: var(--red); font-size: 74px; letter-spacing: 1px; }
  .headline-days { font-family: "Advent Pro", Arial, sans-serif; font-weight: 200; color: var(--white); font-size: 82px; margin-top: -4px; }
  .headline-word { font-family: "Bebas Neue", Impact, sans-serif; color: var(--navy); font-size: 66px; letter-spacing: 1px; margin-top: -6px; }
  .steps { position: absolute; left: 50px; top: 338px; list-style: none; color: var(--white); font-size: 13.5px; line-height: 20px; }
  .steps b { color: var(--red); font-weight: 400; }
  .pitch { position: absolute; left: 187px; top: 626px; font-size: 17px; color: var(--ink); line-height: 28px; }
  .pitch strong { font-weight: 700; font-size: 19px; }
  .call { position: absolute; left: 178px; top: 707px; font-size: 20px; font-weight: 700; color: var(--red); }
  .call span { color: var(--navy); margin-left: 6px; }
  .links { position: absolute; left: 187px; top: 764px; font-size: 15px; color: var(--ink); }
</style>
</head>
<body>
<div class="poster">
  <div class="crowd-photo" role="img" aria-label="Group photo of smiling adults in business and casual clothing"></div>

  <svg class="swoosh" width="1200" height="800" viewBox="0 0 1200 800" aria-hidden="true">
    <path d="M0,628 C250,575 500,555 700,556 C900,560 1080,620 1200,690 L1200,800 L0,800 Z" fill="var(--white)"/>
    <path d="M640,556 C850,552 1050,570 1200,600 L1200,690 C1000,630 820,590 640,556 Z" fill="var(--red)"/>
    <path d="M0,628 C250,575 500,555 700,556 C900,560 1080,620 1200,690 L1200,790 C1060,680 880,600 700,575 C480,565 240,590 0,634 Z" fill="var(--navy)"/>
  </svg>

  <div class="brand"><span class="brand-mark"></span>RIDGEPOINT CHIROPRACTIC</div>

  <h1 class="headline">
    <div class="headline-name">GLOW RIDGE</div>
    <div class="headline-days">21 DAY</div>
    <div class="headline-word">Challange</div>
  </h1>

  <ul class="steps">
    <li><b>G</b> - Glow Relax Supplements</li>
    <li><b>L</b> - Lean Protein Every Meal</li>
    <li><b>O</b> - Omega 3 supplements</li>
    <li><b>W</b> - Water, 8 Glasses a Day</li>
    <li><b>R</b> - Rest 8 Hours Nightly</li>
    <li><b>I</b> - Improve Posture Daily</li>
    <li><b>D</b> - Daily Vit D Supplements</li>
    <li><b>G</b> - Gut Homemade Probiotic</li>
    <li><b>E</b> - Eat Fruts + Veggies</li>
  </ul>

  <p class="pitch"><strong>Do you have?</strong> Allergies, Need to lose weight,<br>Feel tired, Have Neck or back Pain, contain water weight</p>

  <p class="call">Call today for Details: <span>555-302-4418</span></p>

  <p class="links">www.rgchiropractic..com,&nbsp; www.socialpage.example/rgchiropractor, updates.example/glowridgeDC</p>
</div>
</body>
</html>
```